Help me create an amazing cover for my first ebook!!

I am looking to have a modern and professional looking cover for my first ebook. It will be published through Borvex Quill Self Press and will need to follow their formatting and guidelines. I want the cover to have a modern and vibrant feel, that appeals to a millennial audience. This is a real estate book that is focused on a niche category catered to young professionals, so the idea would be to appeal to them.

Title:
The Twentysomething Playbook for Duplex Living

A Smart Property Buying Plan to Start Early, Cut Your Housing Costs (Sometimes to Zero), and Speed Up Your Path to Lasting Wealth.

Davin Osterlund

Target Market(s)

Real Estate investors, investors, millennials, young professionals, college educated, 20-40 years old.Financial freedom, finance.

Industry/Entity Type

Real Estate

Font styles to use
Sans Serif

Colors

Designer to choose colors to be used in the design.

Requirements
Must have
• Must follow the borvex quill self press format. I attached a screenshot of the details, it can also be found here: https://qsp.borvexbooks.example/en_US/help/topic/R481736025
• Must include this title:
• The Twentysomething Playbook for Duplex Living
• A Smart Property Buying Plan to Start Early, Cut Your Housing Costs (Sometimes to Zero), and Speed Up Your Path to Lasting Wealth.
• Davin Osterlund.
• I added examples of book covers I like to use as a guide, I also added some color pallette examples.
Nice to have
• Modern, clean design that's not too busy. Some sort of simple photo or illustration to incorporate in the cover along with the text would be nice.

```html
<!DOCTYPE html>
<html lang="en">
<head>
<meta charset="utf-8">
<title>The Twentysomething Playbook for Duplex Living — Davin Osterlund</title>
<link rel="stylesheet" href="https://fonts.googleapis.com/css2?family=Anton&family=Oswald:wght@500;600&display=swap">
<style>
  :root {
    --sky-top: #6f86d8;
    --sky-mid: #8f9be0;
    --dusk-pink: #d7a6c4;
    --house-slate: #5a6a9c;
    --ground: #8d92b8;
    --title-blue: #1627a0;
    --title-red: #ea0f1c;
    --rule-navy: #1e2573;
    --frame-line: rgba(30, 34, 70, 0.55);
  }
  html, body {
    margin: 0;
    padding: 0;
    width: 750px;
    height: 1200px;
    overflow: hidden;
    background: #ffffff;
  }
  .cover {
    position: relative;
    width: 750px;
    height: 1200px;
    overflow: hidden;
  }
  .cover-photo {
    position: absolute;
    inset: 0;
    background:
      radial-gradient(ellipse 70% 30% at 68% 62%, rgba(70, 82, 140, 0.75), transparent 70%),
      linear-gradient(180deg,
        var(--sky-top) 0%,
        var(--sky-mid) 30%,
        var(--dusk-pink) 52%,
        var(--house-slate) 64%,
        var(--ground) 82%,
        #c9cde6 100%);
  }
  .frame {
    position: absolute;
    left: 18px;
    top: 30px;
    width: 708px;
    height: 1150px;
    border: 1.5px solid var(--frame-line);
    box-sizing: border-box;
  }
  .author {
    position: absolute;
    right: 50px;
    top: 56px;
    margin: 0;
    font-family: "Oswald", sans-serif;
    font-weight: 600;
    font-size: 38px;
    letter-spacing: 2px;
    color: var(--title-red);
    text-transform: uppercase;
    line-height: 1;
  }
  .title {
    position: absolute;
    left: 40px;
    top: 118px;
    margin: 0;
    font-family: "Anton", sans-serif;
    font-weight: 400;
    text-transform: uppercase;
    line-height: 1;
  }
  .title-line {
    display: block;
    height: 136px;
    font-size: 122px;
    letter-spacing: 1px;
    text-shadow: 3px 4px 3px rgba(20, 20, 50, 0.45);
  }
  .title-line--blue { color: var(--title-blue); }
  .title-line--red { color: var(--title-red); }
  .title-line--long {
    font-size: 86px;
    height: 136px;
    line-height: 1.45;
  }
  .rule {
    position: absolute;
    left: 38px;
    width: 674px;
    height: 6px;
    background: var(--rule-navy);
  }
  .rule--top { top: 964px; }
  .rule--bottom { top: 1166px; }
  .subtitle {
    position: absolute;
    left: 50px;
    width: 650px;
    top: 990px;
    margin: 0;
    font-family: "Oswald", sans-serif;
    font-weight: 500;
    font-size: 30px;
    line-height: 50px;
    text-align: center;
    text-transform: uppercase;
    color: var(--title-red);
    letter-spacing: -0.3px;
  }
</style>
</head>
<body>
  <main class="cover">
    <div class="cover-photo" role="img" aria-label="Photograph of a modern two-storey suburban house with grey siding, a double garage and glowing windows under a blue and pink dusk sky, reflected in a wet driveway"></div>
    <div class="frame"></div>

    <p class="author">Davin Osterlund</p>

    <h1 class="title">
      <span class="title-line title-line--blue">The</span>
      <span class="title-line title-line--blue title-line--long">Twentysomething</span>
      <span class="title-line title-line--blue">Playbook</span>
      <span class="title-line title-line--red">For</span>
      <span class="title-line title-line--red">Duplex</span>
      <span class="title-line title-line--red">Living</span>
    </h1>

    <div class="rule rule--top"></div>
    <p class="subtitle">A Smart Property Buying Plan to Start Early, Cut Your Housing Costs (Sometimes to Zero), and Speed Up Your Path to Lasting Wealth</p>
    <div class="rule rule--bottom"></div>
  </main>
</body>
</html>
```